Need Business cards

Im a new realtor and already have a logo. I would like to purchase a Business card design that catches customer's attention, its creative, and modern.

Marisol Vandera
Realtor ®
(555) 214 7730
marisolvndrealtor@brightmailbox.com

Target Market(s)

investors, buyers and seller, property management

Industry/Entity Type

real estate,

Contact Information for Business Card

Marisol Vandera

Requirements
Must have
• BOTH LOGOS, WOULD LIKE TO SEE WITH DIFFERENT OPTIONS WITH EITHER PICTURE

```html
<!DOCTYPE html>
<html lang="en">
<head>
<meta charset="utf-8">
<title>Marisol Vandera — Realtor Business Card</title>
<link rel="stylesheet" href="https://fonts.googleapis.com/css2?family=Montserrat:wght@400;500;600;700&display=swap">
<style>
  :root {
    --backdrop: #3f3e45;
    --card-black: #1a1a1a;
    --photo-dark: #161616;
    --photo-warm: #8a6a4e;
    --band-blue: #1b3a66;
    --band-text: #5b9bd8;
    --gold: #d2a42a;
    --white: #ffffff;
    --ink: #2b2b2b;
    --rule: #b08a2e;
  }
  * { box-sizing: border-box; margin: 0; padding: 0; }
  html, body {
    width: 1200px; height: 900px; overflow: hidden;
    background: var(--backdrop);
    font-family: "Montserrat", sans-serif;
  }
  .canvas {
    width: 1200px; height: 900px;
    display: flex; flex-direction: column; align-items: center; justify-content: center;
    gap: 50px;
  }
  .card {
    width: 600px; height: 343px;
    box-shadow: 0 10px 28px rgba(0,0,0,0.45);
    overflow: hidden;
  }

  /* Front */
  .card-front {
    background: var(--card-black);
    display: flex; align-items: center; justify-content: center;
  }
  .brand-lockup {
    display: flex; flex-direction: column; align-items: center; gap: 10px;
  }
  .brand-mark {
    display: flex; align-items: center; gap: 12px;
  }
  .brand-square {
    width: 18px; height: 18px; background: var(--gold);
  }
  .brand-name {
    color: var(--gold); font-weight: 600; font-size: 30px; letter-spacing: 3px;
  }
  .brand-role {
    display: flex; align-items: center; gap: 10px;
    color: var(--gold); font-weight: 600; font-size: 14px; letter-spacing: 4px;
  }
  .brand-role::before, .brand-role::after {
    content: ""; width: 80px; height: 1px; background: var(--rule);
  }

  /* Back */
  .card-back { display: flex; background: var(--white); }
  .agent-photo {
    width: 222px; height: 100%;
    background: radial-gradient(ellipse at 55% 55%, var(--photo-warm) 0%, #3a2c22 45%, var(--photo-dark) 80%);
  }
  .broker-band {
    width: 70px; height: 100%;
    background: var(--band-blue);
    display: flex; align-items: center; justify-content: center;
  }
  .broker-name {
    writing-mode: vertical-rl; transform: rotate(180deg);
    color: var(--band-text); font-weight: 700; font-size: 22px; letter-spacing: 3px;
    white-space: nowrap;
  }
  .agent-info {
    flex: 1; padding: 34px 30px 30px 26px;
    display: flex; flex-direction: column; align-items: flex-end;
  }
  .agent-info .brand-lockup { align-self: center; gap: 6px; margin-bottom: 40px; }
  .agent-info .brand-square { width: 11px; height: 11px; }
  .agent-info .brand-name { font-size: 17px; letter-spacing: 2px; }
  .agent-info .brand-role { font-size: 9px; letter-spacing: 3px; }
  .agent-info .brand-role::before, .agent-info .brand-role::after { width: 46px; }
  .agent-name { color: var(--gold); font-weight: 700; font-size: 26px; }
  .agent-title { color: var(--ink); font-size: 14px; margin: 2px 0 26px; }
  .contact-line {
    display: flex; align-items: center; gap: 8px;
    color: var(--ink); font-size: 12.5px; margin-top: 6px;
  }
  .contact-line svg { width: 13px; height: 13px; fill: var(--gold); flex: none; }
</style>
</head>
<body>
<main class="canvas">
  <section class="card card-front">
    <div class="brand-lockup">
      <div class="brand-mark"><span class="brand-square"></span><span class="brand-name">MARISOL VANDERA</span></div>
      <div class="brand-role">REALTOR</div>
    </div>
  </section>

  <section class="card card-back">
    <div class="agent-photo" role="img" aria-label="Portrait photo of the realtor in a black top against a dark background"></div>
    <div class="broker-band"><span class="broker-name">NORTHVALE REALTY</span></div>
    <div class="agent-info">
      <div class="brand-lockup">
        <div class="brand-mark"><span class="brand-square"></span><span class="brand-name">MARISOL VANDERA</span></div>
        <div class="brand-role">REALTOR</div>
      </div>
      <div class="agent-name">Marisol Vandera</div>
      <div class="agent-title">Realtor ®</div>
      <div class="contact-line">(555) 214 7730
        <svg viewBox="0 0 24 24" aria-hidden="true"><path d="M6.6 10.8a15.1 15.1 0 0 0 6.6 6.6l2.2-2.2a1 1 0 0 1 1-.25 11.4 11.4 0 0 0 3.6.57 1 1 0 0 1 1 1V20a1 1 0 0 1-1 1A17 17 0 0 1 3 4a1 1 0 0 1 1-1h3.5a1 1 0 0 1 1 1c0 1.25.2 2.45.57 3.6a1 1 0 0 1-.25 1z"/></svg>
      </div>
      <div class="contact-line">marisolvndrealtor@brightmailbox.com
        <svg viewBox="0 0 24 24" aria-hidden="true"><path d="M2 5h20v14H2z M4 7v.5l8 5 8-5V7l-8 5z" fill-rule="evenodd"/></svg>
      </div>
    </div>
  </section>
</main>
</body>
</html>
```